Photographer Card

I'm currently doing freelance photography and i need a creative design name card especially when i attend events.
I require a design that makes a STATEMENT.
Simple, elegant and nothing like the usual name cards ive seen around (Example: with a camera/tripod etc in the design).

Photographer: Brent LW
Mobile: +65 91846257
E-mail: Brent.LW.Photography@mailvento.com
Facebook: www.friendspage.com/brent.lw.photography

Thanks for your time and hope it will turn out well! :)

Thanks for all your inputs!

Im liking the cursive feel.

Id prefer not to include the title "freelance"  :)

Also, im looking for a logo to establish myself

http://www.artnookgallery.com/art/Pebbles-Business-Card-506213847

Hi all! Thanks for the designs

"Capturing magical moments"
"Capturing magical moments that are gone forever"

Back design can be in big font "look HERE"

Maybe with focusing box 

Names can be played with horizontal and vertical.

Camera

Script

```html
<!DOCTYPE html>
<html lang="en">
<head>
<meta charset="utf-8">
<title>Brent LW – Photographer Card</title>
<link href="https://fonts.googleapis.com/css2?family=Delius&display=swap" rel="stylesheet">
<style>
  :root {
    --backdrop: #a2b2b5;
    --card-black: #060707;
    --ink-white: #ffffff;
    --ink-silver: #e6e6e6;
    --swirl-violet: #3a1d5c;
    --swirl-deep: #1a1024;
    --lens-rim: #2a2b2d;
    --lens-core: #0b0c0d;
  }
  html, body {
    margin: 0;
    width: 1200px;
    height: 1000px;
    overflow: hidden;
    background: var(--backdrop);
  }
  .business-card {
    position: absolute;
    left: 82px;
    top: 187px;
    width: 1036px;
    height: 625px;
    background: var(--card-black);
    overflow: hidden;
    font-family: "Delius", cursive;
  }
  .decor {
    position: absolute;
    inset: 0;
  }
  .card-name {
    position: absolute;
    left: 88px;
    top: 42px;
    margin: 0;
    font-weight: 400;
    font-size: 104px;
    line-height: 1;
    letter-spacing: 4px;
    font-variant: small-caps;
    color: var(--ink-white);
  }
  .card-name-reflection {
    position: absolute;
    left: 88px;
    top: 110px;
    margin: 0;
    font-size: 104px;
    line-height: 1;
    letter-spacing: 4px;
    font-variant: small-caps;
    color: var(--ink-white);
    transform: scaleY(-1);
    opacity: 0.35;
    -webkit-mask-image: linear-gradient(to top, rgba(0,0,0,1) 0%, rgba(0,0,0,0) 45%);
    mask-image: linear-gradient(to top, rgba(0,0,0,1) 0%, rgba(0,0,0,0) 45%);
  }
  .card-title {
    position: absolute;
    left: 66px;
    top: 222px;
    width: 528px;
    margin: 0;
    padding-left: 0;
    font-size: 60px;
    line-height: 1;
    letter-spacing: 3px;
    font-variant: small-caps;
    color: var(--ink-silver);
    border-bottom: 2px solid var(--ink-silver);
    padding-bottom: 0;
    text-indent: 0;
  }
</style>
</head>
<body>
  <div class="business-card">
    <svg class="decor" width="1036" height="625" viewBox="0 0 1036 625">
      <defs>
        <radialGradient id="swirl-glow" cx="0.4" cy="0.45" r="0.6">
          <stop offset="0" stop-color="var(--swirl-violet)" stop-opacity="0.55"/>
          <stop offset="1" stop-color="var(--swirl-deep)" stop-opacity="0"/>
        </radialGradient>
        <radialGradient id="lens-glow" cx="0.5" cy="0.5" r="0.5">
          <stop offset="0" stop-color="var(--lens-core)"/>
          <stop offset="0.55" stop-color="#141516"/>
          <stop offset="0.85" stop-color="var(--lens-rim)"/>
          <stop offset="1" stop-color="#101112"/>
        </radialGradient>
      </defs>
      <g role="img" aria-label="Soft violet light swirl decoration">
        <rect x="0" y="0" width="300" height="625" fill="url(#swirl-glow)"/>
      </g>
      <g role="img" aria-label="Camera lens illustration">
        <circle cx="908" cy="493" r="235" fill="url(#lens-glow)"/>
      </g>
    </svg>
    <p class="card-name-reflection" aria-hidden="true">Brent LW</p>
    <h1 class="card-name">Brent LW</h1>
    <p class="card-title">Photographer</p>
  </div>
</body>
</html>
```